Company Values Graphic

We are looking for a design of our company values that can be used in a variety of places including our website, mousepads, office posters, business cards, etc.

Notes:
- We'd rather have icons/art than photographs on the poster.... so more like an infographic
- The core value group headings are not required, but can be included if you think grouping the values works for your design
- We have a logo for our software product but that logo is not required
- We don't need/want clever images to accompany each value, but some images are fine
- BrightNest logo attached
- BrightNest colors are attached
- BrightNest logo is Nunito Sans ExtraBold 800
- BrightNest website uses Roboto

Our Values - Who we will work with (and who we will not)
The right set of values are essential to building and maintaining a culture that we all wake up eager to be a part of each day. They are foundational to all hiring and firing decisions. They attract the right people and repel the wrong ones.

BE HELPFUL
Make every person and place better because you are there.
Deliver wow with every interaction.

BE HUMBLE
Listen with every muscle.
Passionately help others first.
Seek first to understand.

BE HONEST
Earn trust every day.
Be open and direct.
Treat everyone with fairness and respect.

BE HUMAN
Celebrate passion and action.
Create an environment where people are authentic.
Hire great people and expect a lot from them

BE COURAGEOUS
Dare mighty things.
Make and honor commitments.
All great things start with a small act of courage applied at the right moment.

```html
<!DOCTYPE html>
<html lang="en">
<head>
<meta charset="utf-8">
<title>BrightNest — Our Values</title>
<link rel="stylesheet" href="https://fonts.googleapis.com/css2?family=Montserrat:wght@300;500;900&family=Roboto:wght@400;700&display=swap">
<style>
  :root {
    --navy: #1a1e35;
    --yellow: #ffbe00;
    --orange: #ff5a00;
    --red: #e00000;
    --white: #ffffff;
  }
  * { margin: 0; padding: 0; box-sizing: border-box; }
  html, body { width: 1200px; height: 1200px; overflow: hidden; background: var(--navy); }
  .values-poster {
    position: relative;
    width: 1200px;
    height: 1200px;
    background: var(--navy);
    font-family: "Roboto", Arial, sans-serif;
  }
  .artwork { position: absolute; inset: 0; }
  .heading { font-family: "Montserrat", Arial, sans-serif; }
  .heading--light { font-weight: 300; }
  .heading--medium { font-weight: 500; }
  .heading--heavy { font-weight: 900; }

  .value-line {
    position: absolute;
    font-size: 21px;
    line-height: 23px;
    letter-spacing: 0.3px;
  }
  .value-line--orange { color: var(--orange); }
  .value-line--red { color: var(--red); }
  .value-line--right { text-align: right; }

  .brand {
    position: absolute;
    left: 0; right: 0;
    top: 1050px;
    display: flex;
    justify-content: center;
    align-items: center;
    gap: 16px;
  }
  .brand__dot {
    width: 56px; height: 56px;
    border-radius: 50%;
    background: var(--orange);
  }
  .brand__name {
    font-family: "Roboto", Arial, sans-serif;
    font-weight: 700;
    font-size: 52px;
    color: var(--white);
    letter-spacing: -0.5px;
  }
</style>
</head>
<body>
<main class="values-poster">
  <svg class="artwork" width="1200" height="1200" viewBox="0 0 1200 1200" xmlns="http://www.w3.org/2000/svg">
    <!-- central "be" letterforms -->
    <g class="be-mark" role="img" aria-label="be" fill="none" stroke="var(--yellow)">
      <rect x="342" y="142" width="23" height="617" fill="var(--yellow)" stroke="none"/>
      <ellipse cx="472" cy="626" rx="96" ry="127" stroke-width="22"/>
      <path d="M817 620 A105 127 0 1 0 792 716" stroke-width="22"/>
      <path d="M607 620 H829" stroke-width="20"/>
    </g>

    <!-- value headings -->
    <text class="heading heading--light" x="380" y="289" font-size="133" fill="var(--orange)" textLength="493" lengthAdjust="spacingAndGlyphs">HUMBLE</text>
    <text class="heading heading--heavy" x="479" y="408" font-size="137" fill="var(--red)" textLength="568" lengthAdjust="spacingAndGlyphs">HELPFUL</text>
    <text class="heading heading--heavy" x="355" y="876" font-size="128" fill="var(--red)" textLength="455" lengthAdjust="spacingAndGlyphs">HUMAN</text>
    <text class="heading heading--heavy" transform="translate(256 137) rotate(90)" font-size="94" fill="var(--orange)" textLength="614" lengthAdjust="spacingAndGlyphs">COURAGEOUS</text>
    <text class="heading heading--medium" transform="translate(846 492) rotate(90)" font-size="100" fill="var(--orange)" textLength="384" lengthAdjust="spacingAndGlyphs">HONEST</text>

    <!-- icon areas -->
    <rect class="icon-area" role="img" aria-label="Icon: person raising a flag on a mountain peak" x="173" y="132" width="83" height="126" rx="8" fill="var(--red)"/>
    <rect class="icon-area" role="img" aria-label="Icon: tree with roots below the ground" x="902" y="139" width="141" height="156" rx="10" fill="var(--red)"/>
    <rect class="icon-area" role="img" aria-label="Icon: two people giving a high five" x="371" y="302" width="100" height="94" rx="8" fill="var(--orange)"/>
    <rect class="icon-area" role="img" aria-label="Icon: striped heart" x="161" y="790" width="162" height="142" rx="10" fill="var(--orange)"/>
    <rect class="icon-area" role="img" aria-label="Icon: four hands joined together" x="940" y="781" width="96" height="87" rx="8" fill="var(--red)"/>
  </svg>

  <!-- Humble -->
  <p class="value-line value-line--orange" style="left:381px; top:136px;">Listen with<br>every muscle</p>
  <p class="value-line value-line--orange" style="left:562px; top:136px;">Passionately help<br>others first</p>
  <p class="value-line value-line--orange" style="left:770px; top:139px;">Seek first to<br>understand</p>

  <!-- Helpful -->
  <p class="value-line value-line--red" style="left:480px; top:418px;">Make every person and place<br>better because you are there</p>
  <p class="value-line value-line--red" style="left:845px; top:418px;">Deliver wow with<br>every interaction</p>

  <!-- Courageous -->
  <p class="value-line value-line--orange value-line--right" style="right:954px; top:287px; line-height:25px;">Dare<br>mighty<br>things</p>
  <p class="value-line value-line--orange value-line--right" style="right:954px; top:408px; line-height:25px;">Make and<br>honor<br>commitments</p>
  <p class="value-line value-line--orange value-line--right" style="right:954px; top:549px; line-height:25.5px;">All great<br>things<br>start with a<br>small act<br>of courage<br>applied<br>at the right<br>moment</p>

  <!-- Honest -->
  <p class="value-line value-line--orange" style="left:935px; top:489px;">Earn trust<br>every day</p>
  <p class="value-line value-line--orange" style="left:935px; top:566px;">Be open<br>and direct</p>
  <p class="value-line value-line--orange" style="left:935px; top:643px;">Treat<br>everyone<br>with<br>fairness<br>and respect</p>

  <!-- Human -->
  <p class="value-line value-line--red" style="left:355px; top:895px; line-height:25px;">Celebrate passion<br>and action</p>
  <p class="value-line value-line--red" style="left:547px; top:895px; line-height:25px;">Create an environment<br>where people are authentic</p>
  <p class="value-line value-line--red" style="left:831px; top:895px; line-height:25px;">Hire great people and<br>expect a lot from them</p>

  <footer class="brand">
    <span class="brand__dot" aria-hidden="true"></span>
    <span class="brand__name">BrightNest</span>
  </footer>
</main>
</body>
</html>
```